Harbor Outreach company is looking for a web page design

Your projects should contain:

1. Header: Logo provided by us.
2. Top nav bar: offer, about us, experience, contact.
3. “Choose language” button.
4. Main section: panoramic picture (static, professional, modern).
5. Below section: 3 blocks (image+title+description), which represent our 3 main activities (titles):
• Market Research,
• Marketing Plans,
• Marketing Project.
6. ‘Contact us’ form – Message (text: “Write your message and give us details about your company and activities”), Email, SEND).
7. Page footer: (4 section: Contact, Social Media, Blog, Partners).

Hello!

I uploaded new file 'general_look', which is our idea how the page should generally look like.

BUT! it doesn't mean that your projects should look exactly like this project e.g.:
* titles Market Research, Marketing Plans, Marketing Project can be above these: Image 1,2,3.
* everything doesn't have to be in square and rectangle shape. You can try to manipulate with blocks and can add elipse elemnts or something similar.

We will appreciate your innovative ideas. Just wanted to give you general plan of the site and ilustrate all elements that we require.

Best Regards,
Tomas

IMPORTENT

Please remember that the main picture should be panoramic. Please do not close it in frame.

Small and middle sized companies, which would like to export their goods and services abroad and are interested in raising funds from European Union to expand their activities. These are rather industrial companies with low level of innovativeness. Our mission is to build image of the client’s company and increase awareness of their products to improve their competitiveness and innovativeness.

It Company

• 1. Create designs of main page and subpage.
2. Subpage: Logo, Header, language button, place for article, navigation menu on the right side - below it “contact us” button , footer on the bottom. (In this section we are looking mainly for the design of the header and navigation menu).
3. The whole design should be a series of horizontal blocks.
4. Your projects should be associated with features such as: Reliability, Security, Professionalism, Openness, Uniqueness.
5. The design should be simple, fresh, readable, easy to use and should create a feeling of high quality services.
6. Possibility to change the panoramic picture (separate layer in a graphic file).
7. All pictures and blocks should be static, no movements.
8. Style of the page should be compliant with the logo design, font: Swiss.
9. Designs that we like: http://www.quillbrand-studio.pl/, http://www.zephyrlane-example.com/.
• There shouldn’t be any distractions and not matching parts (whole design should be compact and easy to interpret and remember).

```html
<!DOCTYPE html>
<html lang="en">
<head>
<meta charset="utf-8">
<title>Harbor Outreach</title>
<link href="https://fonts.googleapis.com/css2?family=Ubuntu:wght@400;500;700&family=PT+Sans:wght@400;700&family=Roboto+Condensed:wght@400&display=swap" rel="stylesheet">
<style>
:root{
  --navy:#0b4a78;
  --navy-dark:#063a62;
  --page-grey:#e4e5e7;
  --footer:#222222;
  --footer-rule:#555555;
  --text-grey:#444444;
  --white:#ffffff;
}
*{margin:0;padding:0;box-sizing:border-box}
html,body{width:1184px;height:1200px;overflow:hidden}
body{position:relative;background:var(--page-grey);font-family:"PT Sans",Arial,sans-serif;color:var(--text-grey)}
.abs{position:absolute}

.header{left:0;top:0;width:1184px;height:131px;background:linear-gradient(#e6e7e9 0%,#e2e3e5 75%,#c9cacc 100%)}
.brand{left:201px;top:24px;display:flex;align-items:center;gap:10px}
.brand-dot{width:62px;height:62px;border-radius:50%;background:var(--navy)}
.brand-name{font-family:"Ubuntu",sans-serif;font-weight:500;font-size:34px;color:var(--navy);letter-spacing:-.5px;line-height:1}

.lang-label{left:750px;top:59px;font-size:12.5px;color:#111}
.lang-select{left:851px;top:57px;width:133px;height:21px;background:#fff;border:1px solid #cfd0d2;font-size:12px;color:#111;padding:2px 5px}
.lang-select .arrow{position:absolute;right:1px;top:1px;width:21px;height:17px}

.hero{left:0;top:131px;width:1184px;height:272px;background:linear-gradient(180deg,#3e3350 0%,#7a5d86 30%,#a06c6c 55%,#3a2a22 75%,#1a1410 100%)}
.hero-arrow{top:248px}

.nav{left:201px;top:110px;width:783px;height:43px;border-radius:4px;background:linear-gradient(#1d5e8e 0%,var(--navy) 50%,var(--navy-dark) 100%);display:flex;justify-content:center;align-items:center}
.nav a{font-family:"Roboto Condensed",sans-serif;font-size:16px;color:var(--white);text-decoration:none;letter-spacing:-.2px}
.nav .sep{width:13px;height:13px;border:3px solid var(--white);border-radius:50%;margin:0 44px}

.card-photo{top:384px;width:237px;height:120px;border:2px solid var(--navy)}
.card-title{top:513px;width:237px;height:50px;background:linear-gradient(#0c4a78,#1f6396);color:#fff;font-family:"Ubuntu",sans-serif;font-size:18px;display:flex;align-items:center;justify-content:center;gap:5px}
.card-title b{font-weight:700}
.card-body{top:563px;width:237px;height:134px;border:1px solid #c9cacc;border-top:none;padding:8px 7px;font-size:11px;line-height:13.6px;text-align:justify;color:#333}

.message{left:0;top:706px;width:1184px;height:238px;background:var(--navy)}
.message h2{position:absolute;left:203px;top:22px;font-family:"Ubuntu",sans-serif;font-weight:700;font-size:23px;color:#fff}
.msg-box{left:202px;top:61px;width:391px;height:124px;background:#fff;border:2px solid #c8d4de;padding:14px 12px;font-size:11px;color:#333;white-space:nowrap}
.email-box{left:627px;top:61px;width:357px;height:49px;background:#fff;border:2px solid #c8d4de;border-radius:3px;padding:16px;font-size:12px;color:#333}
.send{left:627px;top:136px;width:357px;height:49px;background:linear-gradient(#d8dbde,#e9eaeb);border-radius:3px;font-family:"Ubuntu",sans-serif;font-weight:500;font-size:28px;color:var(--navy);display:flex;align-items:center;justify-content:center}

.strip{left:0;top:944px;width:1184px;height:22px;background:#cfd0d2}
.footer{left:0;top:966px;width:1184px;height:234px;background:var(--footer);color:#fff}
.fcol{top:18px;width:169px}
.fcol h3{font-family:"Ubuntu",sans-serif;font-weight:500;font-size:23px;padding-bottom:5px;border-bottom:1px solid var(--footer-rule)}
.contact-list{list-style:none;margin-top:12px;font-size:11px}
.contact-list li{height:29.5px;display:flex;align-items:flex-start;gap:6px;white-space:nowrap}
.contact-list li::before,.blog li::before{content:"";width:7px;height:7px;border:2px solid #fff;border-radius:50%;flex:none;margin-top:3px}
.social{list-style:none;margin-top:7px}
.social li{display:flex;align-items:center;gap:11px;height:40px;padding-left:6px;font-size:12px;font-weight:700}
.social .ico{width:32px;height:32px;border-radius:50%;border:2px solid #ddd}
.blog{list-style:none;margin-top:10px;font-size:11px;line-height:13.6px;text-align:justify}
.blog li{display:flex;gap:6px;margin-bottom:12px}
.partners{display:grid;grid-template-columns:48px 48px;gap:20px 24px;margin:14px 0 0 21px}
.partners span{width:48px;height:48px;border-radius:50%}
</style>
</head>
<body>

<div class="abs header"></div>
<div class="abs brand">
  <div class="brand-dot"></div>
  <div class="brand-name">Harbor Outreach</div>
</div>
<div class="abs lang-label">Choose language:</div>
<div class="abs lang-select">English
  <svg class="arrow" viewBox="0 0 21 17"><rect width="21" height="17" fill="#0b4a78"/><path d="M6 6h9l-4.5 6z" fill="#fff"/></svg>
</div>

<div class="abs hero" role="img" aria-label="Panoramic city skyline at dusk with a river, a large observation wheel and a lit parliament clock tower"></div>
<svg class="abs hero-arrow" style="left:199px" width="26" height="40" viewBox="0 0 26 40"><path d="M22 3 6 20l16 17" fill="none" stroke="#fff" stroke-width="5"/></svg>
<svg class="abs hero-arrow" style="left:958px" width="26" height="40" viewBox="0 0 26 40"><path d="M4 3l16 17L4 37" fill="none" stroke="#fff" stroke-width="5"/></svg>

<nav class="abs nav">
  <a href="#">OFFER</a><span class="sep"></span>
  <a href="#">ABOUT US</a><span class="sep"></span>
  <a href="#">EXPERIENCE</a><span class="sep"></span>
  <a href="#">CONTACT</a>
</nav>

<div class="abs card-photo" style="left:201px;background:linear-gradient(120deg,#e8efe6,#c9d8c4 50%,#3a3e44)" role="img" aria-label="Printed bar charts with a pencil and a calculator"></div>
<div class="abs card-title" style="left:201px"><b>MARKET</b> RESEARCH</div>
<div class="abs card-body" style="left:201px">It is a long established fact that a reader will be distracted by the readable content of a page when looking at its layout. The point of using Lorem Ipsum is that it has a more-or-less normal distribution of letters, as opposed to using 'Content here, content here', making it look like readable English.</div>

<div class="abs card-photo" style="left:475px;background:linear-gradient(120deg,#f0eeea,#d6d2cc 55%,#4a3024)" role="img" aria-label="Hand holding a printed pie chart report"></div>
<div class="abs card-title" style="left:475px"><b>MARKET</b> PLANS</div>
<div class="abs card-body" style="left:475px">It is a long established fact that a reader will be distracted by the readable content of a page when looking at its layout. The point of using Lorem Ipsum is that it has a more-or-less normal distribution of letters, as opposed to using 'Content here, content here', making it look like readable English.</div>

<div class="abs card-photo" style="left:746px;background:linear-gradient(100deg,#2aa3d8,#e07a3a 45%,#9aa4ad)" role="img" aria-label="Street advertising billboard with bright orange balloons"></div>
<div class="abs card-title" style="left:746px"><b>MARKET</b> PROJECT</div>
<div class="abs card-body" style="left:746px">It is a long established fact that a reader will be distracted by the readable content of a page when looking at its layout. The point of using Lorem Ipsum is that it has a more-or-less normal distribution of letters, as opposed to using 'Content here, content here', making it look like readable English.</div>

<section class="abs message">
  <h2>Message</h2>
  <div class="abs msg-box">Write your message and give details about your company and activities.</div>
  <div class="abs email-box">Your Email:</div>
  <div class="abs send">SEND</div>
</section>

<div class="abs strip"></div>
<footer class="abs footer">
  <div class="abs fcol" style="left:200px">
    <h3>Contact</h3>
    <ul class="contact-list">
      <li><span><b>Phone:</b> +XX - XXXXXXXXX</span></li>
      <li><span><b>Fax:</b> +XX - XXXXXXXXX</span></li>
      <li><span><b>Email:</b> info@harbor.example</span></li>
      <li><span><b>Web:</b> www.harbor.example</span></li>
    </ul>
  </div>
  <div class="abs fcol" style="left:407px">
    <h3>Social Media</h3>
    <ul class="social">
      <li><span class="ico" style="background:#3b5998"></span>Friendwall</li>
      <li><span class="ico" style="background:#2aa0d8"></span>Chirpline</li>
      <li><span class="ico" style="background:#c8453a"></span>Circlenet +</li>
    </ul>
  </div>
  <div class="abs fcol" style="left:611px">
    <h3>Blog</h3>
    <ul class="blog">
      <li><span>Dummy text ever since the 1500s, when an unknown printer took a galley of type and scrambled it to make a type specimen book.</span></li>
      <li><span>Lorem Ipsum has been the industry's standard dummy text ever since the 1500s, when an unknown printer took a galley of type and scrambled it.</span></li>
    </ul>
  </div>
  <div class="abs fcol" style="left:816px">
    <h3>Partners</h3>
    <div class="partners">
      <span style="background:#c4283a"></span>
      <span style="background:#d83a2e"></span>
      <span style="background:#5a5e64"></span>
      <span style="background:#e8e8e8"></span>
    </div>
  </div>
</footer>

</body>
</html>
```